Veterinary Pylon

My veterinary clinic is not clearly visible from the street and I want to place a Pylon next to my driveway. I want a modern, elegant straight Design, the Photo shows the sheduled place. One can see the clinic on our Homepage: www.fernhollow-tierpraxis.at
The last pictures are examples for pylones I like

Target Market(s)

the passing cars often miss my entry...I want to show where to turn left

Colors
3276b5
33a6d7
00a990

Requirements
Must have
• High value, simple elegance, size: 250cm (high) x 100cm (width)
Nice to have
• Our Logo, arrow(?)

A special Text is not necessary but this will be an option:

Biegen sie hier ab und wir biegen es wieder hin!
Should not have
• Too much Color, the colors I have chosen are the possible colors but it‘s not necessary to use them.

```html
<!DOCTYPE html>
<html lang="de">
<head>
<meta charset="utf-8">
<title>Fernhollow Tierpraxis – Pylon</title>
<link rel="stylesheet" href="https://fonts.googleapis.com/css2?family=Archivo+Black&display=swap">
<style>
  :root {
    --navy: #124b93;
    --sky: #2ebcdf;
    --paper: #ffffff;
  }
  html, body {
    margin: 0;
    padding: 0;
    width: 1200px;
    height: 3000px;
    overflow: hidden;
    background: var(--paper);
  }
  .pylon {
    position: relative;
    width: 1200px;
    height: 3000px;
    background: var(--paper);
    overflow: hidden;
  }
  .brand {
    position: absolute;
    left: 0;
    top: 360px;
    width: 1200px;
    text-align: center;
    font-family: "Archivo Black", "Arial Black", sans-serif;
    color: var(--navy);
    text-transform: uppercase;
    line-height: 1;
  }
  .brand-name {
    display: block;
    font-size: 150px;
    letter-spacing: -2px;
  }
  .brand-sub {
    display: block;
    margin-top: 40px;
    font-size: 74px;
    letter-spacing: 22px;
    padding-left: 22px;
  }
  .brand-rule {
    position: absolute;
    left: 232px;
    top: 710px;
    width: 770px;
    height: 9px;
    background: var(--navy);
  }
  .turn-arrow {
    position: absolute;
    left: 0;
    top: 0;
  }
  .waves {
    position: absolute;
    left: 0;
    top: 0;
  }
  .pet-artwork {
    position: absolute;
    left: 221px;
    top: 2423px;
    width: 841px;
    height: 577px;
    border-radius: 200px 260px 0 0;
    background: radial-gradient(ellipse at 55% 55%, rgba(255,255,255,0.30), rgba(255,255,255,0.08) 70%, rgba(255,255,255,0) 100%);
  }
</style>
</head>
<body>
<main class="pylon">
  <div class="brand">
    <span class="brand-name">Fernhollow</span>
    <span class="brand-sub">Tierpraxis</span>
  </div>
  <div class="brand-rule"></div>

  <svg class="turn-arrow" width="1200" height="3000" viewBox="0 0 1200 3000" aria-label="Pfeil nach links">
    <polyline points="593,1448 449,1593 593,1737" fill="none" stroke="var(--navy)" stroke-width="30" stroke-linecap="butt"/>
    <line x1="466" y1="1593" x2="819" y2="1593" stroke="var(--navy)" stroke-width="30"/>
  </svg>

  <svg class="waves" width="1200" height="3000" viewBox="0 0 1200 3000" aria-hidden="true">
    <path d="M0,1744 C210,1775 400,1850 567,1994 C360,2015 170,2090 0,2200 Z" fill="var(--sky)"/>
    <path d="M0,2277 C250,2080 520,1994 798,1994 C950,1994 1090,2025 1200,2062 L1200,3000 L0,3000 Z" fill="var(--navy)"/>
  </svg>

  <div class="pet-artwork" role="img" aria-label="Weiße Silhouette von Hund und Katze mit Herzschlaglinie"></div>
</main>
</body>
</html>
```